New Cloud Backups MSP - Online Backups - DR - IT Support

My new MSP company offers low cost IT Support and online backups and DR using VaultHarbor solutions.

Some examples of competitors would include;

http://www.quillnetra.com.au/
http://www.pelmoria.com.au/

We require a designer to work closely with us to develop and implement a new website with a signup portal for customers, costing calculators and just general information.

If possible we would also like a new logo designed to complement the new website (as an additional cost)

Target Market(s)

Companies looking for online backups
Companies looking for cost effective IT support

Industry/Entity Type

It Company

Font styles to use
Sans Serif

Colors

Designer to choose colors to be used in the design.

Requirements
Must have
• 'Menu' of services offered
Request a quote form

```html
<!DOCTYPE html>
<html lang="en">
<head>
<meta charset="utf-8">
<title>Brennick Cloud — A MSP Company</title>
<link href="https://fonts.googleapis.com/css2?family=Arimo:wght@400;700&family=Roboto+Condensed:wght@700&display=swap" rel="stylesheet">
<style>
:root{
  --navy:#3a5590;
  --heading:#2f4a86;
  --text:#555;
  --nav:#555;
  --grey-btn:#5f646b;
  --footer:#3b5a9a;
  --line:#d9d9d9;
  --white:#fff;
}
*{box-sizing:border-box;margin:0;padding:0}
html,body{width:1126px;height:1200px;overflow:hidden;background:var(--white);font-family:"Arimo",Arial,sans-serif;color:var(--text)}
.page{position:relative;width:1126px;height:1200px}

/* header */
.site-header{position:absolute;left:0;top:0;width:1126px;height:100px}
.brand{position:absolute;left:169px;top:28px;text-align:right;width:185px}
.brand-name{display:block;font-weight:700;font-size:25px;color:var(--navy);letter-spacing:-1px;line-height:1}
.brand-tag{display:block;font-size:13px;color:#444;margin-top:3px}
.contact{position:absolute;left:545px;top:24px;display:flex;gap:16px;font-size:9px;color:#555;align-items:center}
.contact span{display:flex;align-items:center;gap:5px}
.search{position:absolute;left:766px;top:21px;width:191px;height:19px;border:1px solid #ddd;font-size:8px;color:#999;padding:4px 7px}
.search svg{position:absolute;right:4px;top:3px}
.main-nav{position:absolute;left:425px;top:63px;width:532px;display:flex;justify-content:space-between;font-size:11px;color:var(--nav)}

/* hero */
.hero{position:absolute;left:0;top:100px;width:1126px;height:372px;
  background:linear-gradient(180deg,#1c3568 0%,#3c5f98 35%,#8aa6cb 62%,#dfe6ef 85%,#eef1f5 100%)}
.hero-art{position:absolute;left:170px;top:70px;width:375px;height:260px;border-radius:40% 40% 20% 20%;
  background:radial-gradient(ellipse at 50% 55%,#2a9fd0 0%,#1a6a98 40%,rgba(210,230,245,.6) 75%,rgba(255,255,255,0) 100%)}
.hero-title{position:absolute;left:591px;top:186px;font-family:"Arimo",Arial,sans-serif;font-weight:700;font-size:40px;color:var(--white);letter-spacing:-.5px}
.hero-text{position:absolute;left:591px;top:245px;width:370px;font-size:12px;line-height:20px;color:var(--white)}
.hero-btn{position:absolute;left:593px;top:319px;width:163px;height:41px;border:1px solid #c8ccd2;border-radius:2px;
  background:linear-gradient(#fafafa,#dfe2e6);color:var(--heading);font-size:14px;display:flex;align-items:center;justify-content:center}
.hero-arrow{position:absolute;top:265px}
.hero-arrow.prev{left:109px}.hero-arrow.next{left:985px}

/* content */
.section-title{font-family:"Roboto Condensed","Arial Narrow",sans-serif;font-weight:700;color:var(--heading);font-size:15px;text-transform:uppercase}
.welcome{position:absolute;left:169px;top:490px;width:790px}
.welcome p{margin-top:12px;font-size:8px;line-height:18px}
.service{position:absolute;top:602px;width:241px}
.service .section-title{padding-left:3px}
.service-photo{margin-top:20px;width:241px;height:137px}
.service p{margin-top:19px;font-size:8px;line-height:17.7px}
.read-more{display:flex;align-items:center;justify-content:center;margin-top:11px;width:85px;height:28px;border-radius:2px;background:linear-gradient(#6c7178,#4e5359);color:var(--white);font-size:10px}
.photo-support{background:linear-gradient(120deg,#2d6fbf 0%,#6aa5e0 55%,#e6eef6 100%)}
.photo-backups{background:linear-gradient(100deg,#c9d2dd 0%,#6f8aa8 35%,#1b1b1d 65%,#0b0b0c 100%)}
.photo-dr{background:radial-gradient(ellipse at 55% 55%,#9c7a62 0%,#4a3a32 35%,#0d0d0d 70%)}

.features{position:absolute;left:169px;top:949px;display:flex;gap:15px}
.feature{width:186px;height:67px;border:1px solid #d6d6d6;background:linear-gradient(#fff,#f2f2f2);position:relative}
.feature svg{position:absolute;left:11px;top:14px}
.feature h3{position:absolute;left:72px;top:12px;font-weight:400;font-size:12px;color:var(--heading)}
.feature p{position:absolute;left:72px;top:31px;width:110px;font-size:7.5px;line-height:14.5px;color:#444}

.partners{position:absolute;left:0;top:1043px;width:1126px;height:78px;border-top:1px solid var(--line);
  display:flex;align-items:center;justify-content:space-between;padding:0 180px 0 176px}
.partner{font-size:14px;font-weight:700;color:#6c7686}

/* footer */
.site-footer{position:absolute;left:0;top:1121px;width:1126px;height:79px;background:var(--footer);color:var(--white)}
.footer-brand{position:absolute;left:170px;top:25px;display:flex;align-items:center;gap:7px;font-size:17px;font-weight:400}
.footer-brand i{width:12px;height:12px;border-radius:50%;background:var(--white);display:block}
.footer-divider{position:absolute;left:320px;top:20px;width:1px;height:45px;background:rgba(255,255,255,.4)}
.footer-nav{position:absolute;left:342px;top:21px;font-size:8.5px;display:flex;gap:11px}
.copyright{position:absolute;left:342px;top:47px;font-size:8.5px}
.social{position:absolute;left:832px;top:25px;display:flex;gap:7px}
.social span{width:25px;height:25px;border-radius:50%;background:rgba(255,255,255,.22);border:1px solid rgba(255,255,255,.35)}
</style>
</head>
<body>
<div class="page">

<header class="site-header">
  <div class="brand">
    <span class="brand-name">Brennick Cloud</span>
    <span class="brand-tag">A MSP Company</span>
  </div>
  <div class="contact">
    <span><svg width="8" height="12" viewBox="0 0 8 12"><rect x=".5" y=".5" width="7" height="11" rx="1.2" fill="none" stroke="#777"/><rect x="2" y="2" width="4" height="6" fill="#777"/></svg>( 1048 ) 220 317</span>
    <span><svg width="12" height="9" viewBox="0 0 12 9"><rect width="12" height="9" fill="#777"/><path d="M0 0l6 5 6-5" fill="none" stroke="#fff"/></svg>hello@brennickcloud.net</span>
  </div>
  <div class="search">Search :
    <svg width="11" height="11" viewBox="0 0 11 11"><circle cx="4.5" cy="4.5" r="3.5" fill="none" stroke="#bbb" stroke-width="1.3"/><path d="M7 7l3 3" stroke="#bbb" stroke-width="1.5"/></svg>
  </div>
  <nav class="main-nav">
    <span>Home</span><span>About Us</span><span>Services</span><span>Solutions</span><span>Support</span><span>Contact us</span>
  </nav>
</header>

<section class="hero">
  <div class="hero-art" role="img" aria-label="Illustration of server racks standing in a glossy blue cloud shape"></div>
  <svg class="hero-arrow prev" width="32" height="32" viewBox="0 0 32 32" aria-hidden="true"><circle cx="16" cy="16" r="14" fill="none" stroke="#5d7fb4" stroke-width="2" opacity=".5"/><path d="M19 9l-7 7 7 7" fill="none" stroke="#5d7fb4" stroke-width="3" opacity=".5"/></svg>
  <svg class="hero-arrow next" width="32" height="32" viewBox="0 0 32 32" aria-hidden="true"><circle cx="16" cy="16" r="14" fill="none" stroke="#5d7fb4" stroke-width="2"/><path d="M13 9l7 7-7 7" fill="none" stroke="#5d7fb4" stroke-width="3"/></svg>
  <h1 class="hero-title">Brennick Cloud</h1>
  <p class="hero-text">We provide low cost IT Support and online backups and DR using VaultHarbor solutions. So use the vaultharbor logo in footer somewhere.</p>
  <a class="hero-btn">View more details</a>
</section>

<section class="welcome">
  <h2 class="section-title">Welcome to Brennick Cloud</h2>
  <p>It is a long established fact that a reader will be distracted by the readable content of a page when looking at its layout. The point of using Lorem Ipsum is that it has a more-or-less normal distribution of letters, as opposed to using 'Content here, content here', making it look like readable English. Many desktop publishing packages and web page editors now use Lorem Ipsum as their default model text, and a search for 'lorem ipsum' will uncover many web sites still in their infancy. Various versions have evolved over the years, sometimes by accident, sometimes on purpose</p>
</section>

<article class="service" style="left:169px">
  <h2 class="section-title">IT Support</h2>
  <div class="service-photo photo-support" role="img" aria-label="Photo of a man touching a floating transparent screen against a blue sky"></div>
  <p>It is a long established fact that a reader will be distracted by the readable content of a page when looking at its layout. The point of using Lorem Ipsum is that it has a more-or-less normal distribution of letters...</p>
  <a class="read-more">Read More</a>
</article>
<article class="service" style="left:442px">
  <h2 class="section-title">Online Backups</h2>
  <div class="service-photo photo-backups" role="img" aria-label="Photo of a businessman holding a glass globe"></div>
  <p>It is a long established fact that a reader will be distracted by the readable content of a page when looking at its layout. The point of using Lorem Ipsum is that it has a more-or-less normal distribution of letters...</p>
  <a class="read-more">Read More</a>
</article>
<article class="service" style="left:716px">
  <h2 class="section-title">DR using VaultHarbor solutions</h2>
  <div class="service-photo photo-dr" role="img" aria-label="Photo of a woman holding a light bulb and a tablet on a dark background"></div>
  <p>It is a long established fact that a reader will be distracted by the readable content of a page when looking at its layout. The point of using Lorem Ipsum is that it has a more-or-less normal distribution of letters...</p>
  <a class="read-more">Read More</a>
</article>

<section class="features">
  <div class="feature">
    <svg width="52" height="40" viewBox="0 0 52 40" aria-hidden="true"><rect x="2" y="8" width="26" height="28" rx="2" fill="none" stroke="#666" stroke-width="2.5"/><rect x="16" y="4" width="28" height="22" rx="1" fill="#fff" stroke="#666" stroke-width="2.5"/><rect x="38" y="22" width="10" height="16" rx="1.5" fill="#fff" stroke="#666" stroke-width="2.5"/></svg>
    <h3>Lorem Ipsum simply</h3>
    <p>Lorem Ipsum is simply dum my text of the printing.</p>
  </div>
  <div class="feature">
    <svg width="46" height="42" viewBox="0 0 46 42" aria-hidden="true"><rect x="2" y="2" width="42" height="28" rx="2" fill="none" stroke="#666" stroke-width="3"/><path d="M18 31h10l2 8H16z" fill="#666"/></svg>
    <h3>Lorem Ipsum simply</h3>
    <p>Lorem Ipsum is simply dummy text of the printing.</p>
  </div>
  <div class="feature">
    <svg width="46" height="42" viewBox="0 0 46 42" aria-hidden="true"><rect x="10" y="2" width="30" height="38" rx="2" fill="none" stroke="#666" stroke-width="3.5"/></svg>
    <h3>Lorem Ipsum simply</h3>
    <p>Lorem Ipsum is simply dummy text of the printing.</p>
  </div>
  <div class="feature">
    <svg width="46" height="42" viewBox="0 0 46 42" aria-hidden="true"><rect x="14" y="2" width="20" height="38" rx="3" fill="none" stroke="#666" stroke-width="3"/><circle cx="24" cy="34" r="2.5" fill="#666"/></svg>
    <h3>Lorem Ipsum simply</h3>
    <p>Lorem Ipsum is simply dummy text of the printing.</p>
  </div>
</section>

<section class="partners" aria-label="Partners">
  <span class="partner">Tellvora</span>
  <span class="partner">Brindle Cafe</span>
  <span class="partner">Korvex</span>
  <span class="partner">Lumisto</span>
  <span class="partner">Quorant</span>
  <span class="partner">Halden Pryce</span>
  <span class="partner">Vestrum</span>
</section>

<footer class="site-footer">
  <div class="footer-brand"><i></i>VAULTHARBOR</div>
  <div class="footer-divider"></div>
  <nav class="footer-nav">
    <span>Home</span><span>|</span><span>About Us</span><span>|</span><span>Services</span><span>|</span><span>Solutions</span><span>|</span><span>Support</span><span>|</span><span>Contact us</span>
  </nav>
  <p class="copyright">Copyright 2014 © Brennick Cloud. All rights reserved.</p>
  <div class="social" aria-label="Social links"><span></span><span></span><span></span><span></span></div>
</footer>

</div>
</body>
</html>
```